San Francisco Leading Consulting firm - 47Nova Web Design Project

•Create a Web Design
•Uncoded webpage layout design
•2 Pages Design - Homepage + Interior Page

Task Description
Hello, we're looking for a re-design our current website www.47nova-example.com

we have a sample mockup design @

http://47nova.civicpane-example.org/

This shows the layout that we like and also a sample of 6 pictures that would change based on where you mouse over..

6 pictures HOME design needs to be included.

SMART
THOUGHTFUL
FLEXIBLE
CREATIVE SERVICES
TECHNICAL SERVICES
PARTNERS

sites we like:

http://www.brelmoradvisory-example.com/Home.cfm?id=Home
http://www.pixelquarry-example.com/index.html

Our company can be best described as: 100+ employees, cutting-edge, depandable, innovative, strong, smart.

Our Primary focus is: IT Consulting Services and Creative Design services

47Nova LLC is a consulting firm providing creative design, business and technology solutions to both private and public interests.

Established in 1996, 47Nova is a San Francisco based company providing specialists for a range of business needs including:

Creative Design Services
•Print
•Logo Design
•Website Design
•Illustration

and

Business and Technology solutions

•Application Software and Web Development
•Business Process Re-Design (BPR)
•Business/Systems Analysis and Requirement Documentation
•Mentoring and Training
•Network/Hardware Installation Services
•System Design and Architecture
•Vendor Management
•Teamvault Architecture and Implementation

our sample mockup site:

Reason: Due to holiday season, we're not available to work with designers and finilize our design.  

Thank you very much for submitting your design.

We appreciate your time and creativity.   Since, our office is currently closed for holidays, we will be reviewing it in details next week and will make our decision as soon as possible.

It would be great if you could submit any of your changes by Wed next week, so it would be part of our reviews. 

Please see updated wireframe under attachments:  we have some minor updates to our wireframe that we would like you to update your designs, if possible.  

We also encorouge you not to use our standard wireframe and come up with more unique designs.   Everything would be considered when we review your design.

 

Target Market(s)

Creative services and professional services clients, including government agencies

Industry/Entity Type

Business

Requirements
Must have
• Clean, professional look, easy navigation

```html
<!DOCTYPE html>
<html lang="en">
<head>
<meta charset="utf-8">
<title>47Nova — Home</title>
<link rel="stylesheet" href="https://fonts.googleapis.com/css2?family=League+Gothic&family=PT+Sans:wght@400;700&family=Arimo:wght@400;700&display=swap">
<style>
  :root{
    --sky-top:#f4fafd;
    --sky:#cfe7f4;
    --panel:#eeeeee;
    --heading:#555570;
    --body:#4a4a4a;
    --link:#1f8fc4;
    --footer-outer:#46425a;
    --footer-inner:#5a5770;
    --footer-bar:#37344a;
    --login:#4d4a64;
    --hero-light:#8cc9e7;
    --hero-dark:#23779f;
    --dot-active:#6cc3d8;
    --field:#f1f1f1;
    --submit-top:#4fb0c4;
    --submit-bottom:#1f7890;
    --white:#ffffff;
  }
  *{box-sizing:border-box;margin:0;padding:0}
  html,body{width:1200px;height:990px;overflow:hidden}
  body{
    position:relative;
    font-family:"Arimo",Arial,sans-serif;
    color:var(--body);
    background:
      radial-gradient(ellipse 520px 300px at 600px 40px, var(--sky-top), transparent 75%),
      linear-gradient(180deg,#e6f3fa 0,var(--sky) 680px);
  }
  .abs{position:absolute}

  /* header */
  .brand{left:205px;top:38px;display:flex;align-items:center;gap:10px;
    font-family:"PT Sans",sans-serif;font-size:36px;font-weight:400;color:#2b2b33;letter-spacing:1px}
  .brand-dot{width:30px;height:30px;border-radius:50%;background:#2c8cc7}
  .login{left:912px;top:0;width:94px;height:28px;border-radius:0 0 6px 6px;
    background:linear-gradient(180deg,#635f7c,var(--login));color:var(--white);
    font-family:"PT Sans",sans-serif;font-size:14px;text-align:center;line-height:27px}
  .main-nav{left:597px;top:53px;display:flex;gap:0;font-family:"PT Sans",sans-serif;font-size:15px;color:#2e2e36}
  .main-nav a{color:inherit;text-decoration:none;padding:0 11px;height:24px;line-height:24px;border-radius:12px;margin-right:7px}
  .main-nav a.current{background:#e9eef1}

  /* hero */
  .hero{left:193px;top:103px;width:813px;height:310px;border-radius:12px 12px 0 0;overflow:hidden;display:flex}
  .hero-caption{position:relative;width:272px;height:100%;background:linear-gradient(180deg,var(--hero-light),#3d91b8 55%,var(--hero-dark))}
  .hero-title{position:absolute;left:38px;top:40px;font-family:"League Gothic",sans-serif;font-size:58px;line-height:1;color:var(--white)}
  .hero-sub{position:absolute;left:38px;top:98px;font-family:"League Gothic",sans-serif;font-size:21px;line-height:20px;color:var(--white);letter-spacing:.3px}
  .slide-dots{position:absolute;left:40px;top:268px;display:flex;gap:7px}
  .slide-dots span{width:27px;height:27px;border-radius:50%;background:#f3f3f3;color:#444;
    font-family:"League Gothic",sans-serif;font-size:17px;text-align:center;line-height:27px}
  .slide-dots span.active{background:var(--dot-active);color:var(--white)}
  .hero-photo{flex:1;background:radial-gradient(ellipse at 75% 60%,#2e4d45,#132824 60%,#0c1a18)}
  .hero-arrow{width:34px;height:34px;border-radius:50%;background:radial-gradient(circle at 50% 35%,#fff,#e2e2e2);
    box-shadow:0 1px 3px rgba(0,0,0,.25);top:235px}
  .hero-arrow svg{display:block;margin:10px auto}
  .arrow-prev{left:184px}
  .arrow-next{left:983px}

  /* features */
  .features{left:193px;top:413px;width:813px;height:267px;background:var(--panel)}
  .feature{position:absolute;top:30px;width:240px;font-size:10.5px;line-height:19px}
  .feature h2{font-family:"League Gothic",sans-serif;font-weight:400;font-size:30px;line-height:30px;color:var(--heading);margin-bottom:12px}
  .feature .thumb{float:left;width:68px;height:68px;margin:0 15px 4px 0}
  .feature h3{font-size:12px;font-weight:700;color:var(--heading);line-height:14px;margin-bottom:5px}
  .feature a{color:var(--link);text-decoration:none;font-size:10.5px}
  .f1{left:34px}.f2{left:308px}.f3{left:582px}
  .thumb-office{background:linear-gradient(135deg,#dfe3e6,#7a8088 60%,#2c2f33)}
  .thumb-tower{background:linear-gradient(180deg,#5b8fc9,#2c5a3a)}
  .thumb-hands{background:linear-gradient(180deg,#3d7fd0,#a9cdee 60%,#d6b08e)}

  /* footer */
  .footer{left:0;top:680px;width:1200px;height:277px;background:var(--footer-outer)}
  .footer-inner{left:193px;top:680px;width:813px;height:277px;background:var(--footer-inner)}
  .foot-h{font-family:"League Gothic",sans-serif;font-size:27px;line-height:1;color:var(--white);text-align:right;width:200px}
  .foot-text{font-size:10.5px;line-height:17px;color:var(--white);width:205px}
  .foot-links a{display:block;color:var(--white);font-size:10.5px;line-height:20.5px}
  .support-links a{color:var(--white);font-size:10.5px;margin-right:17px}
  .field{left:766px;width:214px;border-radius:6px;background:var(--field);border:1px solid #d8d8d8;
    font-size:10px;color:#9a8fb5;padding:7px 7px}
  .submit{left:766px;top:912px;width:77px;height:23px;border-radius:12px;
    background:linear-gradient(180deg,var(--submit-top),var(--submit-bottom));color:var(--white);
    font-size:10.5px;text-align:center;line-height:23px;box-shadow:0 1px 2px rgba(0,0,0,.3)}
  .footer-bar{left:0;top:957px;width:1200px;height:33px;background:var(--footer-bar)}
  .copyright{right:219px;top:968px;font-size:10.5px;color:var(--white);word-spacing:2px}
</style>
</head>
<body>

<header>
  <div class="abs brand"><span class="brand-dot"></span>47Nova</div>
  <div class="abs login">Login</div>
  <nav class="abs main-nav">
    <a class="current" href="#">Home</a>
    <a href="#">Company</a>
    <a href="#">Services</a>
    <a href="#">Partners</a>
    <a href="#">Contact</a>
  </nav>
</header>

<section class="abs hero">
  <div class="hero-caption">
    <div class="hero-title">SMART</div>
    <div class="hero-sub">WE DON’T BELIEVE IN THE<br>TERM “OVERQUALIFIED.”</div>
    <div class="slide-dots">
      <span class="active">1</span><span>2</span><span>3</span><span>4</span><span>5</span><span>6</span>
    </div>
  </div>
  <div class="hero-photo" role="img" aria-label="Photo of a hand writing equations in chalk on a green chalkboard"></div>
</section>
<div class="abs hero-arrow arrow-prev"><svg width="12" height="14" viewBox="0 0 12 14"><path d="M10 1 L2 7 L10 13 Z" fill="#b8b8b8"/></svg></div>
<div class="abs hero-arrow arrow-next"><svg width="12" height="14" viewBox="0 0 12 14"><path d="M2 1 L10 7 L2 13 Z" fill="#b8b8b8"/></svg></div>

<section class="abs features">
  <article class="feature f1">
    <h2>WE’RE HIRING!</h2>
    <div class="thumb thumb-office" role="img" aria-label="Photo of a computer workstation with keyboard"></div>
    <h3>Get Creative!</h3>
    <p>47Nova is looking for top creative talent to deliver graphic design solutions for some leading global brands. Do you have what it takes?</p>
    <a href="#">Learn More →</a>
  </article>
  <article class="feature f2">
    <h2>OUR SERVICES</h2>
    <div class="thumb thumb-tower" role="img" aria-label="Photo of a glass office tower against blue sky"></div>
    <h3>The 47Nova Difference</h3>
    <p>Smart, Flexible, Thoughtful: Find out why leading corporations and government agencies are turning to 47nova to help manage their most demanding IT services challenges.</p>
    <a href="#">Learn More →</a>
  </article>
  <article class="feature f3">
    <h2>PARTNER WITH US</h2>
    <div class="thumb thumb-hands" role="img" aria-label="Photo of a business handshake under blue sky"></div>
    <h3>Team Up With The Best</h3>
    <p>When it comes to technology partnerships, our mission it to make you a success.</p>
    <a href="#">Learn More →</a>
  </article>
</section>

<footer>
  <div class="abs footer"></div>
  <div class="abs footer-inner"></div>

  <div class="abs foot-h" style="left:179px;top:711px">ABOUT 47NOVA</div>
  <p class="abs foot-text" style="left:398px;top:710px">47Nova provides professional experience in all phases of IT projects from vendor selection to post production support.</p>

  <div class="abs foot-h" style="left:179px;top:790px">SUPPORT</div>
  <div class="abs support-links" style="left:398px;top:790px"><a href="#">Help &amp; FAQ</a><a href="#">Email us</a></div>

  <div class="abs foot-h" style="left:179px;top:835px">LINKS</div>
  <div class="abs foot-links" style="left:398px;top:833px">
    <a href="#">Lorem ipsum dolor sit amet</a>
    <a href="#">Nam sed neque quis dui rhoncus</a>
    <a href="#">Sed id eros lacus, nec feugiat tellus</a>
    <a href="#">Quisque pharetra felis vitae dui</a>
  </div>

  <div class="abs foot-h" style="left:555px;top:711px">CONTACT</div>
  <div class="abs field" style="top:712px;height:26px">Name</div>
  <div class="abs field" style="top:746px;height:26px">Email</div>
  <div class="abs field" style="top:781px;height:118px">Message</div>
  <div class="abs submit">Submit</div>

  <div class="abs footer-bar"></div>
  <div class="abs copyright">Copyright © 2010. 47Nova, LLC. All rights reserved.</div>
</footer>

</body>
</html>
```